Velmor Haulden cargo van wrap design

Looking for a new wrap design for 2020 velmor Haulden 310 cargo van
Looking for a sleek and luxury looking design in satin black
We offer Mobile Window Tinting
Also would like to add detailing ,ppf and wrap as subtexts
I would be attaching my logo and current van design
Also feel free to redesign my logo if needed
Might be considering to fully redesign logo if it looks better

Industry/Entity Type

Window tinting, auto detailing

Colors

Designer to choose colors to be used in the design.

```html
<!DOCTYPE html>
<html lang="en">
<head>
<meta charset="utf-8">
<title>Dark Vale – Van Rear Wrap</title>
<link rel="stylesheet" href="https://fonts.googleapis.com/css2?family=Anton&family=Oswald:wght@500;700&display=swap">
<style>
  :root {
    --backdrop: #ececec;
    --wrap-white: #ffffff;
    --satin-black: #0d0d0d;
    --band-black: #161616;
    --headline: #262626;
    --silver: #d9d9d9;
    --seam: #8a8a8a;
    --contour: #5a5a5a;
  }
  html, body {
    margin: 0;
    padding: 0;
    width: 1200px;
    height: 800px;
    overflow: hidden;
    background: var(--backdrop);
  }
  .canvas {
    width: 1200px;
    height: 800px;
    display: flex;
    align-items: center;
    justify-content: center;
  }
  .rear-wrap {
    width: 620px;
    height: 690px;
    display: block;
  }
  .headline-main {
    font-family: "Anton", "Oswald", sans-serif;
    font-size: 132px;
    fill: var(--headline);
    letter-spacing: 4px;
  }
  .headline-sub {
    font-family: "Oswald", sans-serif;
    font-weight: 700;
    font-size: 74px;
    fill: var(--headline);
    letter-spacing: 4px;
  }
  .brand-name {
    font-family: "Oswald", sans-serif;
    font-weight: 500;
    font-size: 96px;
    fill: var(--silver);
    letter-spacing: 3px;
  }
</style>
</head>
<body>
<main class="canvas">
  <svg class="rear-wrap" viewBox="680 210 890 960" xmlns="http://www.w3.org/2000/svg" role="img" aria-label="Rear door wrap for the Dark Vale window tinting van">
    <defs>
      <clipPath id="panel-shape">
        <path d="M730 1160 L690 780 L700 520 Q735 265 800 236 Q1120 214 1450 236 Q1512 265 1540 520 L1560 780 L1520 1160 Z"/>
      </clipPath>
    </defs>

    <g clip-path="url(#panel-shape)">
      <rect class="panel-base" x="680" y="210" width="890" height="960" fill="var(--wrap-white)"/>

      <rect class="divider-band" x="680" y="478" width="890" height="42" fill="var(--band-black)"/>
      <polygon class="side-stripe-left" points="680,478 760,478 680,640" fill="var(--band-black)"/>
      <polygon class="side-stripe-right" points="1480,478 1570,478 1570,660" fill="var(--band-black)"/>

      <polygon class="lower-field" points="790,575 1440,575 1570,770 1570,1170 680,1170 680,770" fill="var(--satin-black)"/>

      <path class="door-contour" d="M745 735 Q1120 850 1505 725" fill="none" stroke="var(--contour)" stroke-width="4"/>
      <line class="door-seam" x1="1122" y1="240" x2="1122" y2="1160" stroke="var(--seam)" stroke-width="2" opacity="0.6"/>
    </g>

    <text class="headline-main" x="1115" y="385" text-anchor="middle">WINDOW</text>
    <text class="headline-sub" x="1113" y="460" text-anchor="middle">TINTING SERVICE</text>

    <g class="brand-lockup">
      <rect class="brand-square" x="840" y="628" width="62" height="62" fill="var(--silver)"/>
      <text class="brand-name" x="930" y="694">DARK VALE</text>
    </g>
  </svg>
</main>
</body>
</html>
```